Lumo - Booking activities for Kids and Adults.

The app allows booking of Kid's activities for a given date/time.
The app lists activities offered via various clubs (vendors) which a user can book for their kids.
The users can browse various clubs and their offered activities. The users can manage their kid's profiles.
Need a whole new look to the app. The existing app can be checked out at
https://apps.storefrontx.example/details?id=com.lumokw
https://appmarket.example/us/app/lumo-لومو/id9827315064?ls=1
Try using the app as Guest.

Target Market(s)

Kuwait

Font styles to use
Serif
Sans Serif

Requirements
Must have
• Home Screens
The home page should have everything from the existing app and a quick area to change between different kid's profile to see activities matching their interests ONLY. In the current version, there's no switch profile and hence we are showing the name tags on the activities.

We are also going to build ecommerce so we need that ecommerce look and feel.
Kindly maintain the image aspect ratio from the current app so the new version doesn't require new images.

Need a complete new innovative designs - Keep the color scheme same.
The designs should be minimalistic and image oriented. The design should be done in XD. The designs should be submitted in both light and dark theme.
Reference to be used - http://trevlan.example.uk

D.M for more info if needed.

```html
<!DOCTYPE html>
<html lang="en">
<head>
<meta charset="utf-8">
<title>Lumo – Booking Confirmation</title>
<link href="https://fonts.googleapis.com/css2?family=Poppins:wght@400;500;600;700&display=swap" rel="stylesheet">
<style>
  :root {
    --bg: #eef1f8;
    --white: #ffffff;
    --ink: #3d3a55;
    --ink-soft: #5a5870;
    --cyan: #00dcdc;
    --orange: #f7931e;
    --blue-tag: #5eb4f0;
    --pink-tag: #ef5a8c;
    --grey-pill: #e8e9ee;
    --nova-blue: #0a76a8;
    --purple: #2a1b4d;
  }
  * { box-sizing: border-box; margin: 0; padding: 0; }
  html, body { width: 1200px; height: 2591px; overflow: hidden; }
  body { background: var(--bg); font-family: 'Poppins', sans-serif; color: var(--ink); position: relative; }

  .app-header {
    position: absolute; left: 0; top: 0; width: 1200px; height: 327px;
    background: var(--white); border-radius: 0 0 80px 80px;
    box-shadow: 0 10px 30px rgba(60,60,110,.05);
  }
  .menu-dots { position: absolute; left: 62px; top: 203px; display: flex; gap: 11px; }
  .menu-dots span { width: 20px; height: 20px; border-radius: 50%; background: var(--ink); }
  .brand {
    position: absolute; left: 0; right: 0; top: 160px; text-align: center;
    font-size: 84px; font-weight: 500; color: var(--orange); line-height: 1;
  }

  .success-icon { position: absolute; left: 527px; top: 439px; width: 150px; height: 150px; }
  .page-title {
    position: absolute; left: 0; right: 0; top: 620px; text-align: center;
    font-size: 82px; font-weight: 700; line-height: 1.2;
  }
  .page-note {
    position: absolute; left: 40px; right: 40px; top: 737px; text-align: center;
    font-size: 35px; line-height: 45px; color: var(--ink);
  }

  .booking-card {
    position: absolute; left: 62px; width: 1078px; height: 575px;
    background: var(--white); border-radius: 26px;
    box-shadow: 0 14px 40px rgba(60,60,110,.06);
  }
  .vendor-logo {
    position: absolute; left: 74px; top: 93px; width: 178px; height: 179px;
    border-radius: 26px; display: flex; align-items: center; justify-content: center;
  }
  .vendor-logo.nova { background: var(--nova-blue); color: var(--white); font-size: 40px; font-weight: 700; }
  .vendor-logo.soccer { background: var(--purple); }
  .vendor-name {
    position: absolute; left: 0; width: 326px; top: 295px; text-align: center;
    font-size: 27px; font-weight: 600; color: var(--ink);
  }
  .vendor-area {
    position: absolute; left: 0; width: 326px; top: 330px; text-align: center;
    font-size: 24px; color: var(--ink-soft);
  }
  .tags { position: absolute; left: 321px; top: 93px; display: flex; gap: 8px; }
  .tag {
    height: 40px; padding: 0 27px; border-radius: 20px; color: var(--white);
    font-size: 22px; font-weight: 600; line-height: 40px;
  }
  .tag.sara { background: var(--blue-tag); }
  .tag.fahad { background: var(--pink-tag); padding: 0 22px; }
  .activity-title {
    position: absolute; left: 321px; top: 139px; font-size: 48px; font-weight: 600; line-height: 1.2;
  }
  .price-row { position: absolute; left: 321px; top: 202px; display: flex; align-items: center; gap: 22px; }
  .price-now { font-size: 45px; font-weight: 700; color: var(--orange); line-height: 1.2; }
  .price-was {
    background: var(--grey-pill); border-radius: 19px; padding: 0 32px; height: 37px; line-height: 37px;
    font-size: 19px; font-weight: 500; color: var(--ink); text-decoration: line-through;
  }
  .details { position: absolute; left: 327px; top: 268px; font-size: 29px; line-height: 48px; color: var(--ink-soft); }
  .actions { position: absolute; left: 643px; top: 446px; display: flex; gap: 11px; }
  .action {
    width: 64px; height: 64px; border-radius: 12px; display: flex; align-items: center; justify-content: center;
  }
  .action.call { background: var(--grey-pill); }
  .action.calendar { background: var(--cyan); }
  .action.directions {
    width: 228px; background: var(--orange); color: var(--white); font-size: 26px; font-weight: 600; gap: 10px;
  }

  .tab-bar {
    position: absolute; left: 5px; top: 2388px; width: 1192px; height: 260px;
    background: var(--cyan); border-radius: 96px;
  }
  .tab { position: absolute; top: 0; width: 240px; text-align: center; color: var(--white); }
  .tab-icon { position: absolute; left: 50%; top: 40px; transform: translateX(-50%); width: 88px; height: 84px; display: flex; align-items: center; justify-content: center; border-radius: 12px; }
  .tab.active .tab-icon { background: var(--orange); }
  .tab-label { position: absolute; left: 0; right: 0; top: 124px; font-size: 31px; font-weight: 700; }
</style>
</head>
<body>

<header class="app-header">
  <div class="menu-dots"><span></span><span></span><span></span></div>
  <div class="brand">Lumo</div>
</header>

<svg class="success-icon" viewBox="0 0 150 150" aria-hidden="true">
  <circle cx="75" cy="75" r="75" fill="var(--cyan)"/>
  <path d="M44 78 L66 99 L108 56" fill="none" stroke="#fff" stroke-width="16" stroke-linecap="round" stroke-linejoin="round"/>
</svg>
<h1 class="page-title">Confirmation</h1>
<p class="page-note">A Confirmation email will be sent to your registered mailbox<br>within minutes or you can view your order history on the<br>app.in your Account Your Booking No.#546877</p>

<section class="booking-card" style="top:922px">
  <div class="vendor-logo nova">NOVA</div>
  <div class="vendor-name">Lumo Academy</div>
  <div class="vendor-area">Hawaly</div>
  <div class="tags"><span class="tag sara">SARA</span><span class="tag fahad">FAHAD</span></div>
  <h2 class="activity-title">Engineering Basics</h2>
  <div class="price-row"><span class="price-now">KWD 10.000</span><span class="price-was">KWD 20.000</span></div>
  <div class="details">1 Sessions for 2 children<br>Fri,Sept 21 2018 | 3:00 Pm<br>Hawally Block 2 St 2.<br>Behind The Mall<br>Kuwait</div>
  <div class="actions">
    <div class="action call"><svg width="26" height="26" viewBox="0 0 24 24"><path fill="var(--ink)" d="M6.6 10.8a15.1 15.1 0 0 0 6.6 6.6l2.2-2.2a1 1 0 0 1 1-.25 11.4 11.4 0 0 0 3.6.57 1 1 0 0 1 1 1V20a1 1 0 0 1-1 1A17 17 0 0 1 3 4a1 1 0 0 1 1-1h3.5a1 1 0 0 1 1 1c0 1.25.2 2.45.57 3.57a1 1 0 0 1-.25 1z"/></svg></div>
    <div class="action calendar"><svg width="30" height="30" viewBox="0 0 24 24" fill="none" stroke="#fff" stroke-width="1.6"><rect x="3" y="5" width="18" height="16" rx="2"/><path d="M3 9h18M8 3v4M16 3v4M7 13h2M11 13h2M15 13h2M7 17h2M11 17h2M15 17h2"/></svg></div>
    <div class="action directions"><svg width="18" height="24" viewBox="0 0 12 16"><path fill="#fff" d="M6 0a6 6 0 0 0-6 6c0 4.5 6 10 6 10s6-5.5 6-10a6 6 0 0 0-6-6zm0 8.2A2.2 2.2 0 1 1 6 3.8a2.2 2.2 0 0 1 0 4.4z"/></svg>Directions</div>
  </div>
</section>

<section class="booking-card" style="top:1535px">
  <div class="vendor-logo soccer" role="img" aria-label="Soccer academy emblem with a football"></div>
  <div class="vendor-name">Soccer Academy</div>
  <div class="vendor-area">Hawaly</div>
  <div class="tags"><span class="tag sara">SARA</span><span class="tag fahad">FAHAD</span></div>
  <h2 class="activity-title">Engineering Basics</h2>
  <div class="price-row"><span class="price-now">KWD 10.000</span><span class="price-was">KWD 20.000</span></div>
  <div class="details">1 Sessions for 2 children<br>Fri,Sept 21 2018 | 3:00 Pm<br>Hawally Block 2 St 2.<br>Behind The Mall<br>Kuwait</div>
  <div class="actions">
    <div class="action call"><svg width="26" height="26" viewBox="0 0 24 24"><path fill="var(--ink)" d="M6.6 10.8a15.1 15.1 0 0 0 6.6 6.6l2.2-2.2a1 1 0 0 1 1-.25 11.4 11.4 0 0 0 3.6.57 1 1 0 0 1 1 1V20a1 1 0 0 1-1 1A17 17 0 0 1 3 4a1 1 0 0 1 1-1h3.5a1 1 0 0 1 1 1c0 1.25.2 2.45.57 3.57a1 1 0 0 1-.25 1z"/></svg></div>
    <div class="action calendar"><svg width="30" height="30" viewBox="0 0 24 24" fill="none" stroke="#fff" stroke-width="1.6"><rect x="3" y="5" width="18" height="16" rx="2"/><path d="M3 9h18M8 3v4M16 3v4M7 13h2M11 13h2M15 13h2M7 17h2M11 17h2M15 17h2"/></svg></div>
    <div class="action directions"><svg width="18" height="24" viewBox="0 0 12 16"><path fill="#fff" d="M6 0a6 6 0 0 0-6 6c0 4.5 6 10 6 10s6-5.5 6-10a6 6 0 0 0-6-6zm0 8.2A2.2 2.2 0 1 1 6 3.8a2.2 2.2 0 0 1 0 4.4z"/></svg>Directions</div>
  </div>
</section>

<nav class="tab-bar">
  <div class="tab active" style="left:103px">
    <div class="tab-icon"><svg width="54" height="54" viewBox="0 0 24 24" fill="none" stroke="#fff" stroke-width="1.5"><rect x="3" y="5" width="18" height="16" rx="2"/><path d="M3 9h18M8 3v4M16 3v4M7 13h2M11 13h2M15 13h2M7 17h2M11 17h2M15 17h2"/></svg></div>
    <div class="tab-label">What's On</div>
  </div>
  <div class="tab" style="left:368px">
    <div class="tab-icon"><svg width="54" height="54" viewBox="0 0 24 24" fill="none" stroke="#fff" stroke-width="2.2" stroke-linecap="round"><circle cx="10.5" cy="10.5" r="7"/><path d="M16 16l5 5"/></svg></div>
    <div class="tab-label">Search</div>
  </div>
  <div class="tab" style="left:622px">
    <div class="tab-icon"><svg width="54" height="60" viewBox="0 0 24 26" fill="none" stroke="#fff" stroke-width="2" stroke-linejoin="round"><path d="M5 2h14v22l-7-6-7 6z"/></svg></div>
    <div class="tab-label">Saved</div>
  </div>
  <div class="tab" style="left:855px">
    <div class="tab-icon"><svg width="56" height="56" viewBox="0 0 24 24" fill="none" stroke="#fff" stroke-width="1.8"><circle cx="12" cy="8" r="5"/><path d="M3 23c0-5 4-8 9-8s9 3 9 8"/></svg></div>
    <div class="tab-label">Account</div>
  </div>
</nav>

</body>
</html>
```